One pager Business Profile BrightHire

We would like to create a onepage with our company profile. It is important to keep the basis like it is in the word document but make it nice and fancy. Consistancy in color and fonts is important.

I've added the logo so you can pick the correct colors. The small logo's you can reuse, I want to replace them once you are ready.

In the word document we used standard Word stuff, I would like nice symbols and a professional well designed block in the Cooperation part

I would like to have a source file so I can change (and translate) text, so better to use a regular font or free font (I need the font than).

Target Market(s)

Recruitment

Industry/Entity Type

Recruitment

Requirements
Must have
• a professional look

```html
<!DOCTYPE html>
<html lang="en">
<head>
<meta charset="utf-8">
<title>BrightHire – Business Profile</title>
<link rel="stylesheet" href="https://fonts.googleapis.com/css2?family=Anton&family=Montserrat:wght@600&family=Roboto:ital,wght@0,400;0,500;0,700;1,400&display=swap">
<style>
  :root{
    --blue:#0a7ac4;
    --blue-dark:#0b5aa8;
    --blue-bright:#1e8ff0;
    --blue-pale:#e4f0fa;
    --ink:#3d3d3d;
    --grey:#6a6a6a;
    --grey-bar:#55575a;
    --red:#f04a34;
    --stage:#9a9a9a;
    --paper:#ffffff;
  }
  *{box-sizing:border-box;margin:0;padding:0}
  html,body{width:1200px;height:851px;overflow:hidden}
  body{background:var(--stage);font-family:"Roboto",Arial,sans-serif;color:var(--ink);position:relative}
  .page{position:absolute;top:73px;width:486px;height:688px;background:var(--paper);overflow:hidden}
  .page--front{left:98px}
  .page--back{left:616px}
  .abs{position:absolute}
  .brand{font-family:"Montserrat",sans-serif;font-weight:600;letter-spacing:.04em;color:var(--blue-dark);white-space:nowrap;display:flex;align-items:center;gap:8px}
  .brand i{display:inline-block;width:.55em;height:.55em;background:var(--blue-dark)}

  /* front */
  .front-brand{left:32px;top:24px;font-size:26px}
  .hero{left:0;top:0;width:486px;height:360px}
  .offer-panel{left:264px;top:300px;width:208px;height:375px;background:linear-gradient(180deg,#d6e8f6 0%,var(--blue-pale) 40%,#f3f8fc 100%)}
  .hl{left:37px;font-family:"Anton",sans-serif;color:var(--blue);line-height:1;white-space:nowrap}
  .hl-1{top:354px;font-size:30px}
  .hl-2{top:379px;font-size:73px;letter-spacing:1.5px}
  .hl-3{top:448px;font-size:15.5px}
  .pledge{left:37px;top:472px;font-family:"Anton",sans-serif;font-size:14.5px;line-height:16.4px;color:var(--ink);width:225px}
  .intro{left:37px;top:527px;width:220px;font-size:10.6px;line-height:12.6px;color:var(--grey)}
  .rule{left:37px;top:578px;width:56px;height:2px;background:var(--blue)}
  .claim{left:37px;top:594px;font-size:7.6px;color:var(--blue);text-transform:uppercase}
  .claim-sub{left:37px;top:604px;font-size:6.6px;color:var(--grey);font-style:italic}
  .clients{left:37px;top:622px;width:225px;display:flex;flex-wrap:wrap;gap:4px 10px;font-size:9px;font-weight:700;color:var(--grey)}
  .tab{height:25px;background:var(--blue);color:#fff;font-weight:700;font-size:14px;display:flex;align-items:center;justify-content:center;letter-spacing:.2px}
  .offer-tab{left:282px;top:361px;width:175px}
  .offer-copy{left:281px;top:394px;width:177px;font-size:9.5px;line-height:11.7px;color:var(--grey);text-align:justify}
  .offer-copy p+p{margin-top:4px}
  .contact-tab{left:282px;top:578px;width:175px}
  .front-phone{left:282px;top:606px;font-size:20px;font-weight:700;color:var(--grey);letter-spacing:.2px}
  .front-web{left:284px;top:632px;font-size:10px;color:var(--blue);letter-spacing:3.3px}
  .foot-l{left:0;bottom:0;width:272px;height:11px;background:var(--blue)}
  .foot-r{left:276px;bottom:0;width:210px;height:11px;background:var(--grey-bar)}

  /* back */
  .back-hero{left:0;top:0;width:486px;height:310px}
  .back-brand{right:35px;top:299px;font-size:21px}
  .lead{left:29px;top:331px;width:422px;font-size:11px;line-height:13.6px;color:var(--ink)}
  .bar{height:22px;color:#fff;font-weight:700;font-size:14px;display:flex;align-items:center;padding-left:7px;letter-spacing:.2px}
  .bar--blue{background:var(--blue-dark)}
  .bar--grey{background:var(--grey-bar)}
  .transp-bar{left:29px;top:382px;width:422px}
  .points{left:29px;top:409px;list-style:none;font-size:9.8px;line-height:13.4px;color:var(--ink)}
  .points li{display:flex;align-items:center;gap:5px}
  .expert-bar{left:29px;top:458px;width:203px}
  .coop-bar{left:244px;top:458px;width:207px;padding-left:11px}
  .skills{left:29px;top:489px;list-style:none;font-size:9.5px;line-height:14.8px;color:var(--ink)}
  .skills li{display:flex;align-items:center;gap:6px}
  .skills em{font-style:italic}
  .tick{width:10px;height:10px;flex:none}
  .dot{width:9px;height:9px;flex:none}
  .addr{left:29px;top:620px;font-size:8.5px;color:var(--blue-dark)}
  .back-phone{left:29px;top:631px;font-size:14px;font-weight:700;color:var(--ink)}
  .back-web{left:29px;top:648px;font-size:16px;color:var(--blue-dark)}
  .coop{left:236px;top:487px;width:218px;height:162px}
  .foot-l2{left:0;bottom:0;width:242px;height:11px;background:var(--grey-bar)}
  .foot-r2{left:244px;bottom:0;width:242px;height:11px;background:var(--blue-dark)}
</style>
</head>
<body>
<svg width="0" height="0" style="position:absolute" aria-hidden="true">
  <defs>
    <symbol id="i-tick" viewBox="0 0 10 10"><rect x=".6" y="1.4" width="8" height="8" fill="none" stroke="#0b5aa8" stroke-width="1.2"/><path d="M2.4 5.2l2 2L9.4 1" fill="none" stroke="#0b5aa8" stroke-width="1.6"/></symbol>
    <symbol id="i-dot" viewBox="0 0 10 10"><circle cx="5" cy="5" r="5" fill="#0b5aa8"/><path d="M2.7 5.1l1.6 1.6 3-3.2" fill="none" stroke="#fff" stroke-width="1.4"/></symbol>
  </defs>
</svg>

<!-- Front page -->
<section class="page page--front">
  <svg class="abs hero" viewBox="0 0 486 360">
    <defs>
      <linearGradient id="heroFront" x1="0" y1="0" x2="1" y2="1">
        <stop offset="0" stop-color="#9fb3c4"/><stop offset=".45" stop-color="#d9e4ec"/><stop offset="1" stop-color="#6f7f8e"/>
      </linearGradient>
    </defs>
    <polygon points="0,87 486,62 486,304 0,339" fill="url(#heroFront)" role="img" aria-label="Photo: business people shaking hands in a bright office meeting room"/>
    <polygon points="0,84 486,59 486,65 0,90" fill="var(--blue)"/>
    <polygon points="0,337 486,302 486,307 0,342" fill="var(--blue)"/>
  </svg>
  <div class="abs offer-panel"></div>
  <div class="abs brand front-brand"><i></i>BrightHire</div>

  <div class="abs hl hl-1">BETTER EXPERTS</div>
  <div class="abs hl hl-2">FASTER</div>
  <div class="abs hl hl-3">THE BEST DEVELOPERS IN OUR NETWORK</div>
  <div class="abs pledge">WE OFFER OUR PROFESSIONALS<br>ONLY IF WE ARE CONVINCED OF THEIR<br>COMPETENCES AND SKILLS</div>
  <p class="abs intro">We have access to a specialist network of software development professionals carefully built up over a period of 15 years</p>
  <div class="abs rule"></div>
  <div class="abs claim">By employing qualitatively suitable candidates,</div>
  <div class="abs claim-sub">we receive positive customer reviews &amp; score high customer satisfaction.</div>
  <div class="abs clients">
    <span>Northwind</span><span>Kestrel</span><span>Harbor</span><span>Meridian</span><span>Lumen</span><span>Corvo</span><span>Vantage</span>
  </div>

  <div class="abs tab offer-tab">OUR OFFER</div>
  <div class="abs offer-copy">
    <p>BrightHire helps you solve your IT organisation's capacity problems by offering &amp; deploying high-quality, highly developed candidates.</p>
    <p>Our candidates, our professionals, are driven, and they are used to getting the best out of themselves and their project. They bring up-to-date knowledge for you, so they immediately tap the best level for you as a client to help achieve the objectives of the project, and therefore really complement your team. Our professionals are of immediate value &amp; deliver demonstrable results..</p>
  </div>
  <div class="abs tab contact-tab">CONATCT US</div>
  <div class="abs front-phone">0031 30 55 18 240</div>
  <div class="abs front-web">WWW.BRIGHTHIRE.NL</div>
  <div class="abs foot-l"></div><div class="abs foot-r"></div>
</section>

<!-- Back page -->
<section class="page page--back">
  <svg class="abs back-hero" viewBox="0 0 486 310">
    <defs>
      <linearGradient id="heroBack" x1="0" y1="0" x2="1" y2="0">
        <stop offset="0" stop-color="#c9c2bb"/><stop offset=".35" stop-color="#3f6f9e"/><stop offset="1" stop-color="#2d5f93"/>
      </linearGradient>
    </defs>
    <polygon points="0,0 486,0 486,255 0,297" fill="url(#heroBack)" role="img" aria-label="Photo: professional touching a glowing HR network of people icons"/>
    <polygon points="0,293 486,250 486,257 0,301" fill="var(--blue-dark)"/>
  </svg>
  <div class="abs brand back-brand"><i></i>BrightHire</div>
  <p class="abs lead">As part of the ClearPath Group and our partner network, BrightHire is able to provide clients with full development teams, complete with test automators, scrum masters, product owners and business analysts and developers..</p>

  <div class="abs bar bar--blue transp-bar">TRANSPARANT &amp; OPEN</div>
  <ul class="abs points">
    <li><svg class="dot"><use href="#i-dot"/></svg>BrightHire stands for transparency and openness, for both client &amp; contractor.</li>
    <li><svg class="dot"><use href="#i-dot"/></svg>Clear agreements &amp; no unnecessary obligations.</li>
    <li><svg class="dot"><use href="#i-dot"/></svg>Short lines, &amp; smooth response times. For both the client &amp; the professional.</li>
  </ul>

  <div class="abs bar bar--grey expert-bar">EXPERTISES TEAMS</div>
  <div class="abs bar bar--blue coop-bar">COOPERATION</div>
  <ul class="abs skills">
    <li><svg class="tick"><use href="#i-tick"/></svg>Backend Developers</li>
    <li><svg class="tick"><use href="#i-tick"/></svg>Frontend Developers <em>(web frameworks)</em></li>
    <li><svg class="tick"><use href="#i-tick"/></svg>Platform Developers <svg class="tick"><use href="#i-tick"/></svg>Data Engineers</li>
    <li><svg class="tick"><use href="#i-tick"/></svg>Devops <em>(cloud platforms)</em></li>
    <li><svg class="tick"><use href="#i-tick"/></svg>Scripting Developers</li>
    <li><svg class="tick"><use href="#i-tick"/></svg>Testers <em>(automation &amp; functioneel)</em></li>
    <li><svg class="tick"><use href="#i-tick"/></svg>Mobile Developers <em>(phone / tablet)</em></li>
    <li><svg class="tick"><use href="#i-tick"/></svg>UX/UI Developers</li>
  </ul>
  <div class="abs addr">BrightHire, Lindenlaan 12, 3511 AB Utrecht</div>
  <div class="abs back-phone">CALL US: 0031 30 55 18 240</div>
  <div class="abs back-web">WWW.BRIGHTHIRE.NL</div>

  <svg class="abs coop" viewBox="0 0 218 162" font-family="Roboto, Arial, sans-serif">
    <g fill="var(--blue-bright)" stroke="var(--blue-bright)">
      <line x1="20" y1="8" x2="20" y2="152" stroke-width="1.2"/>
      <path d="M20 3l-3 6h6zM20 157l-3-6h6z" stroke="none"/>
    </g>
    <text transform="translate(12 138) rotate(-90)" font-size="11" fill="var(--ink)" letter-spacing=".3">CUSTOMER RQUEST</text>
    <g font-size="7.6" font-weight="500" fill="#fff" text-anchor="middle">
      <rect x="32" y="4" width="56" height="34" rx="3" fill="#6d7075"/>
      <text x="60" y="19">ClearPath</text><text x="60" y="29">Groep</text>
      <rect x="94" y="4" width="56" height="34" rx="3" fill="#5aa4ec"/>
      <text x="122" y="19">Netwerk</text><text x="122" y="29">Partijen</text>
      <rect x="156" y="4" width="56" height="34" rx="3" fill="var(--red)"/>
      <text x="184" y="24">KLANT</text>
    </g>
    <g stroke="var(--grey)" stroke-width="1.2" fill="var(--grey)">
      <line x1="60" y1="40" x2="60" y2="60"/><path d="M60 64l-3-5h6z" stroke="none"/>
      <line x1="122" y1="40" x2="122" y2="60"/><path d="M122 64l-3-5h6z" stroke="none"/>
      <line x1="184" y1="40" x2="184" y2="60"/><path d="M184 64l-3-5h6z" stroke="none"/>
      <line x1="122" y1="118" x2="122" y2="98"/><path d="M122 94l-3 5h6z" stroke="none"/>
    </g>
    <rect x="32" y="66" width="180" height="28" rx="3" fill="var(--blue-dark)"/>
    <text x="122" y="84" font-size="10" font-weight="700" fill="#fff" text-anchor="middle">BrightHire</text>
    <rect x="32" y="120" width="180" height="34" rx="3" fill="var(--blue-bright)"/>
    <text x="122" y="140" font-size="8" font-weight="500" fill="#fff" text-anchor="middle">ZZP'ers | developers</text>
  </svg>

  <div class="abs foot-l2"></div><div class="abs foot-r2"></div>
</section>
</body>
</html>
```